Banner Design for High End Jewelry Website

We need a banner for our website (brindlestone.com) for a sale that we will be running. The banner should be a size 1187 × 400. I have included a few pieces of jewelry to be included in the banner (do not need to use all, can use just some). The banner should say:
"Christmas is Closer Than You Think Sale!"
Shop Now

Industry/Entity Type

Jewelry

```html
<!DOCTYPE html>
<html lang="en">
<head>
<meta charset="UTF-8">
<title>Brindlestone Christmas Sale Banners</title>
<link rel="stylesheet" href="https://fonts.googleapis.com/css2?family=Pacifico&family=Roboto:wght@300;400;500&display=swap">
<style>
  :root {
    --page-bg: #ffffff;
    --peach: #f6e0d3;
    --blush: #f4c9bd;
    --red: #ff1616;
    --red-deep: #ff0d0d;
    --pink-edge: #f7b7b2;
    --white: #ffffff;
    --subtitle-dark: #5c1515;
    --gold: #d9b04a;
    --gold-soft: #e9cf8d;
    --frame: #b9b0ad;
  }
  * { box-sizing: border-box; margin: 0; padding: 0; }
  html, body {
    width: 1110px;
    height: 1200px;
    overflow: hidden;
    background: var(--page-bg);
  }
  .sheet {
    position: relative;
    width: 1110px;
    height: 1200px;
  }
  .banner {
    position: absolute;
    left: 80px;
    width: 950px;
    height: 320px;
    overflow: hidden;
    border: 1px solid var(--frame);
    box-shadow: 0 1px 2px rgba(0,0,0,0.25);
    background: linear-gradient(90deg,
      var(--peach) 0%,
      #f5d8cb 35%,
      var(--blush) 50%,
      #fb6c66 56%,
      var(--red) 61%,
      var(--red-deep) 72%,
      #ff4a45 80%,
      var(--pink-edge) 90%,
      #f5c4bc 100%);
  }
  .banner--one { top: 40px; }
  .banner--two { top: 440px; }
  .banner--three { top: 840px; }

  .product-visual {
    position: absolute;
    left: 88px;
    top: 24px;
    width: 330px;
    height: 272px;
    border-radius: 46% 46% 40% 40%;
    background: radial-gradient(ellipse at 45% 60%,
      var(--gold) 0%,
      #c99a3a 35%,
      var(--gold-soft) 65%,
      rgba(246,224,211,0) 100%);
  }

  .offer {
    position: absolute;
    left: 554px;
    top: 0;
    width: 240px;
    height: 100%;
    text-align: center;
    color: var(--white);
  }
  .offer__title {
    position: absolute;
    left: 0; right: 0;
    top: 34px;
    font-family: "Pacifico", cursive;
    font-size: 46px;
    line-height: 1.3;
    text-shadow: 0 2px 3px rgba(0,0,0,0.35);
  }
  .offer__subtitle {
    position: absolute;
    left: -20px; right: -20px;
    top: 113px;
    font-family: "Roboto", sans-serif;
    font-weight: 300;
    font-size: 18px;
    letter-spacing: 0.1px;
    color: var(--white);
  }
  .banner--two .offer__subtitle,
  .banner--three .offer__subtitle { color: var(--subtitle-dark); }

  .offer__sale {
    position: absolute;
    left: 0; right: 0;
    top: 136px;
    display: flex;
    justify-content: center;
    align-items: center;
    gap: 12px;
  }
  .offer__sale-word {
    font-family: "Roboto", sans-serif;
    font-weight: 400;
    font-size: 50px;
    line-height: 60px;
    letter-spacing: 1px;
  }
  .snowflake { width: 34px; height: 34px; display: block; }

  .shop-button {
    position: absolute;
    left: 48px;
    top: 224px;
    width: 144px;
    height: 48px;
    border: 1px solid var(--white);
    font-family: "Roboto", sans-serif;
    font-weight: 500;
    font-size: 19px;
    line-height: 46px;
    color: var(--white);
    text-decoration: none;
    background: transparent;
  }
  .banner--two .shop-button,
  .banner--three .shop-button { background: #ff0a0a; }
</style>
</head>
<body>
<svg width="0" height="0" style="position:absolute">
  <defs>
    <g id="flake" stroke="#ffffff" stroke-width="2.4" stroke-linecap="round" fill="none">
      <path d="M17 2v30M4 9.5l26 15M4 24.5l26-15"/>
      <path d="M13 4.5l4 3.5 4-3.5M13 29.5l4-3.5 4 3.5"/>
      <path d="M3 14l5.2-1 1.8-5M31 20l-5.2 1-1.8 5M3 20l5.2 1 1.8 5M31 14l-5.2-1-1.8-5"/>
    </g>
  </defs>
</svg>
<main class="sheet">
  <section class="banner banner--one">
    <div class="product-visual" role="img" aria-label="Gold rings and earrings set with coloured cabochon gemstones and diamonds"></div>
    <div class="offer">
      <h2 class="offer__title">Christmas</h2>
      <p class="offer__subtitle">IS CLOSER THAN YOU THINK</p>
      <div class="offer__sale">
        <svg class="snowflake" viewBox="0 0 34 34" aria-hidden="true"><use href="#flake"/></svg>
        <span class="offer__sale-word">SALE</span>
        <svg class="snowflake" viewBox="0 0 34 34" aria-hidden="true"><use href="#flake"/></svg>
      </div>
      <a class="shop-button" href="#">SHOP NOW</a>
    </div>
  </section>

  <section class="banner banner--two">
    <div class="product-visual" role="img" aria-label="Gold rings and earrings set with coloured cabochon gemstones and diamonds"></div>
    <div class="offer">
      <h2 class="offer__title">Christmas</h2>
      <p class="offer__subtitle">IS CLOSER THAN YOU THINK</p>
      <div class="offer__sale">
        <svg class="snowflake" viewBox="0 0 34 34" aria-hidden="true"><use href="#flake"/></svg>
        <span class="offer__sale-word">SALE</span>
        <svg class="snowflake" viewBox="0 0 34 34" aria-hidden="true"><use href="#flake"/></svg>
      </div>
      <a class="shop-button" href="#">SHOP NOW</a>
    </div>
  </section>

  <section class="banner banner--three">
    <div class="product-visual" role="img" aria-label="Gold rings and earrings set with coloured cabochon gemstones and diamonds"></div>
    <div class="offer">
      <h2 class="offer__title">Christmas</h2>
      <p class="offer__subtitle">IS CLOSER THAN YOU THINK</p>
      <div class="offer__sale">
        <svg class="snowflake" viewBox="0 0 34 34" aria-hidden="true"><use href="#flake"/></svg>
        <span class="offer__sale-word">SALE</span>
        <svg class="snowflake" viewBox="0 0 34 34" aria-hidden="true"><use href="#flake"/></svg>
      </div>
      <a class="shop-button" href="#">SHOP NOW</a>
    </div>
  </section>
</main>
</body>
</html>
```